Veterinary Practice

This is a large and small animal practice that primarily treats cattle,horses,dog and cats. I desire a business card with a picture of each of those animals. I prefer a black cow but the other animals can be any color. The back of the cards needs to have appointment scheduling information.

Industry/Entity Type

Business

Contact Information for Business Card

Copper Hollow Veterinary Services
Dennis M Palk DVM
3847 S Route 41
Wamego KS 66547
785-319-2864

```html
<!DOCTYPE html>
<html lang="en">
<head>
<meta charset="utf-8">
<title>Copper Hollow Veterinary Services – Business Card</title>
<link href="https://fonts.googleapis.com/css2?family=Michroma&family=Teko:wght@500&display=swap" rel="stylesheet">
<style>
  :root {
    --backdrop: #2e2f31;
    --card-light: #e7e9eb;
    --brand-blue: #1aaeea;
    --ink-white: #ffffff;
    --shadow: rgba(0, 0, 0, 0.45);
  }
  * { box-sizing: border-box; margin: 0; padding: 0; }
  html, body {
    width: 1200px;
    height: 816px;
    overflow: hidden;
    background: var(--backdrop);
  }
  .canvas { position: relative; width: 1200px; height: 816px; }
  .business-card {
    position: absolute;
    left: 130px;
    top: 138px;
    width: 940px;
    height: 540px;
    border-radius: 38px;
    background: var(--card-light);
    overflow: hidden;
    box-shadow: 0 24px 50px var(--shadow);
  }
  .brand-panel {
    position: absolute;
    left: 0;
    top: 0;
    width: 400px;
    height: 100%;
  }
  .brand-mark {
    position: absolute;
    left: 165px;
    top: 170px;
    width: 70px;
    height: 70px;
    border-radius: 50%;
    border: 3px solid var(--brand-blue);
  }
  .brand-name {
    position: absolute;
    left: 0;
    top: 300px;
    width: 400px;
    text-align: center;
    font-family: "Michroma", sans-serif;
    font-weight: 400;
    color: var(--brand-blue);
    text-transform: uppercase;
    line-height: 1.5;
  }
  .brand-name .brand-primary {
    display: block;
    font-size: 24px;
    letter-spacing: 1px;
    white-space: nowrap;
  }
  .brand-name .brand-secondary {
    display: block;
    font-size: 13px;
    letter-spacing: 2px;
    white-space: nowrap;
  }
  .contact-panel {
    position: absolute;
    left: 400px;
    top: 0;
    width: 540px;
    height: 100%;
    background: var(--brand-blue);
  }
  .contact-panel .panel-tab {
    position: absolute;
    left: -22px;
    top: 318px;
    width: 0;
    height: 0;
    border-top: 16px solid transparent;
    border-bottom: 16px solid transparent;
    border-right: 22px solid var(--brand-blue);
  }
  .contact-list {
    position: absolute;
    left: 60px;
    top: 48px;
    list-style: none;
    font-family: "Michroma", sans-serif;
    font-size: 15px;
    letter-spacing: 1.5px;
    color: var(--ink-white);
    text-transform: uppercase;
  }
  .contact-item { margin-bottom: 14px; line-height: 1.45; white-space: nowrap; }
  .contact-icon {
    display: block;
    width: 16px;
    height: 16px;
    margin-bottom: 4px;
    fill: var(--ink-white);
  }
  .contact-icon.outline {
    fill: none;
    stroke: var(--ink-white);
    stroke-width: 1.6;
  }
  .dotted-rule {
    position: absolute;
    left: 60px;
    right: 40px;
    top: 318px;
    height: 0;
    border-top: 3px dotted rgba(255, 255, 255, 0.9);
  }
  .person {
    position: absolute;
    right: 45px;
    top: 338px;
    text-align: right;
    font-family: "Teko", sans-serif;
    font-weight: 500;
    color: var(--ink-white);
    text-transform: uppercase;
    line-height: 0.95;
    white-space: nowrap;
  }
  .person-name { font-size: 56px; letter-spacing: 1px; }
  .person-title { font-size: 34px; letter-spacing: 1px; }
</style>
</head>
<body>
<main class="canvas">
  <article class="business-card">
    <section class="brand-panel">
      <span class="brand-mark" aria-hidden="true"></span>
      <h1 class="brand-name">
        <span class="brand-primary">Copper Hollow</span>
        <span class="brand-secondary">Veterinary Services</span>
      </h1>
    </section>

    <section class="contact-panel">
      <span class="panel-tab" aria-hidden="true"></span>
      <ul class="contact-list">
        <li class="contact-item">
          <svg class="contact-icon" viewBox="0 0 16 16" aria-hidden="true">
            <path d="M3.5 1.5l2.5 0 1.2 3.2-1.6 1.2c.8 1.8 2.2 3.2 4 4l1.2-1.6 3.2 1.2v2.5c0 .8-.7 1.5-1.5 1.5C6.9 13.5 2 8.6 2 3c0-.8.7-1.5 1.5-1.5z"/>
          </svg>
          785-319-2864
        </li>
        <li class="contact-item">
          <svg class="contact-icon" viewBox="0 0 16 16" aria-hidden="true">
            <path d="M1 3h14v10H1z M1.8 3.8L8 8.6l6.2-4.8" fill="none" stroke="#fff" stroke-width="1.4"/>
          </svg>
          info@copperhollowvet.com
        </li>
        <li class="contact-item">
          <svg class="contact-icon outline" viewBox="0 0 16 16" aria-hidden="true">
            <circle cx="8" cy="8" r="6.5"/>
            <ellipse cx="8" cy="8" rx="2.8" ry="6.5"/>
            <path d="M1.5 8h13M2.5 4.8h11M2.5 11.2h11"/>
          </svg>
          www.copperhollowvet.com
        </li>
        <li class="contact-item">
          <svg class="contact-icon" viewBox="0 0 16 16" aria-hidden="true">
            <path d="M8 1.5L1 8h2v6.5h3.8v-4h2.4v4H13V8h2z"/>
          </svg>
          3847 S Route 41,<br>Wamego KS 66547
        </li>
      </ul>
      <span class="dotted-rule" aria-hidden="true"></span>
      <div class="person">
        <p class="person-name">Dennis M Palk DVM</p>
        <p class="person-title">General Manager</p>
      </div>
    </section>
  </article>
</main>
</body>
</html>
```